Carver Lindqvist Group Business Cards

We have a new logo, and want to design new business cards with it. We are 21 years in business, and want a fresh but professional look, so not a lot of extra stuff on the card. We are a recruiting and staffing firm focused on placing accounting and finance professionals in the Dallas TX area. I've attached our new logo that should be displayed on the cards. Here is what I think we want on the cards:
Ray Pemberly, CPA
Partner and Managing Director
8282 Orchard Vale Rd.
Suite 610
Dallas, TX 75391
O 214-555-0184
M 214-555-0237
ray@carverlindqvist.example
www.carverlindqvist.example

```html
<!DOCTYPE html>
<html lang="en">
<head>
<meta charset="utf-8">
<title>Carver Lindqvist Group – Business Card</title>
<link rel="stylesheet" href="https://fonts.googleapis.com/css2?family=Lato:wght@400;700&display=swap">
<style>
  :root {
    --backdrop: #e9e7e3;
    --card-top: #ffffff;
    --card-mid: #b9b9dc;
    --card-low: #6e73b8;
    --card-bottom: #1f3a93;
    --brand-blue: #2a3f9c;
    --text-light: #ffffff;
    --text-soft: #eef0fb;
  }
  html, body {
    margin: 0;
    padding: 0;
    width: 1194px;
    height: 1200px;
    overflow: hidden;
    background: var(--backdrop);
    font-family: "Lato", sans-serif;
  }
  .card {
    position: absolute;
    left: 311px;
    top: 100px;
    width: 572px;
    height: 1000px;
    background: linear-gradient(to bottom,
      var(--card-top) 0%,
      var(--card-top) 8%,
      var(--card-mid) 45%,
      var(--card-low) 72%,
      var(--card-bottom) 100%);
    box-shadow: 0 6px 24px rgba(0,0,0,0.18);
  }
  .brand {
    position: absolute;
    top: 225px;
    left: 0;
    width: 100%;
    display: flex;
    justify-content: center;
    align-items: center;
    gap: 14px;
  }
  .brand-mark {
    width: 22px;
    height: 22px;
    background: var(--brand-blue);
  }
  .brand-name {
    font-weight: 700;
    font-size: 30px;
    letter-spacing: 0.5px;
    color: var(--brand-blue);
  }
  .person {
    position: absolute;
    top: 385px;
    left: 150px;
  }
  .person-name {
    margin: 0;
    font-weight: 700;
    font-size: 30px;
    color: var(--brand-blue);
  }
  .person-name .credential {
    font-weight: 400;
    color: var(--text-light);
  }
  .person-title {
    margin: 4px 0 0;
    font-size: 11px;
    letter-spacing: 1.2px;
    text-transform: uppercase;
    color: var(--text-light);
  }
  .contact {
    position: absolute;
    top: 480px;
    left: 150px;
    font-size: 19px;
    line-height: 27px;
    color: var(--text-light);
  }
  .contact p { margin: 0; }
  .contact .phone { letter-spacing: 4px; }
  .contact .email { letter-spacing: 1.5px; }
  .website {
    position: absolute;
    left: 60px;
    bottom: 90px;
    margin: 0;
    font-size: 24px;
    letter-spacing: 4px;
    color: var(--text-soft);
  }
</style>
</head>
<body>
  <article class="card">
    <header class="brand">
      <span class="brand-mark"></span>
      <span class="brand-name">Carver Lindqvist Group</span>
    </header>

    <section class="person">
      <h1 class="person-name">Ray Pemberly<span class="credential">, CPA</span></h1>
      <p class="person-title">Partner and Managing Director</p>
    </section>

    <address class="contact">
      <p>8282 Orchard Vale Rd. Suite 610</p>
      <p>Dallas, TX 75391</p>
      <p class="phone">O 214 555 0184</p>
      <p class="phone">M 214 555 0237</p>
      <p class="email">ray@carverlindqvist.example</p>
    </address>

    <p class="website">www.carverlindqvist.example</p>
  </article>
</body>
</html>
```